LPS AUDITION

I need a post card design (front only) with this on it:
Leap Pulse Stride (this is the main title to be in all caps)
Auditions
Date: Thursday June 30th
6:30-8:30 PM in person
Address: 4172 Kestrel BLVD, Oakland CA 94605
video submissions turn in by Sunday July 3rd, 2022 email:LeapPulseStride22@movenote.test
Teens and Adults welcomed

SO PLEASE COME UP WITH A DESIGN THATS COLORFUL AND INVITING THX!

```html
<!DOCTYPE html>
<html lang="en">
<head>
<meta charset="utf-8">
<title>Leap Pulse Stride Auditions – Postcard</title>
<link href="https://fonts.googleapis.com/css2?family=Krona+One&family=Lexend+Exa:wght@300&family=Montserrat:wght@500;600;700&family=Oswald:wght@500&display=swap" rel="stylesheet">
<style>
  :root {
    --page: #ececec;
    --navy: #0b0d2e;
    --cyan: #08d4d8;
    --blue: #0a5bbb;
    --pink: #d80d74;
    --white: #ffffff;
  }
  * { margin: 0; padding: 0; box-sizing: border-box; }
  html, body { width: 800px; height: 1200px; overflow: hidden; background: var(--page); }
  .postcard {
    position: absolute; left: 0; top: 333px; width: 800px; height: 533px; overflow: hidden;
    background:
      radial-gradient(ellipse 320px 240px at 60px 330px, rgba(30,70,170,.45), transparent 70%),
      radial-gradient(ellipse 360px 300px at 780px 420px, rgba(150,20,90,.55), transparent 70%),
      radial-gradient(ellipse 300px 200px at 600px 40px, rgba(90,30,110,.45), transparent 70%),
      linear-gradient(100deg, var(--navy) 0%, #0e0b24 55%, #2a0c34 100%);
    color: var(--white);
  }
  .dancer-figure {
    position: absolute; left: 560px; top: 34px; width: 230px; height: 484px;
    border-radius: 50% 40% 45% 50% / 30% 30% 60% 60%;
    background: linear-gradient(170deg, #c8207c 0%, #a4238f 45%, #6a2a8a 100%);
    opacity: .85; filter: blur(2px);
  }
  .presenter {
    position: absolute; left: 34px; top: 30px;
    font-family: "Lexend Exa", sans-serif; font-weight: 300;
    font-size: 15px; line-height: 20px; letter-spacing: .5px; color: var(--cyan);
    text-transform: uppercase;
  }
  .title, .schedule { position: absolute; left: 0; top: 0; }
  .auditions {
    position: absolute; left: 40px; top: 236px;
    font-family: "Lexend Exa", sans-serif; font-weight: 300;
    font-size: 42px; line-height: 1; letter-spacing: 4px;
  }
  .address {
    position: absolute; left: 35px; top: 383px;
    font-family: "Montserrat", sans-serif; font-weight: 600; font-size: 18px; line-height: 21px;
    text-transform: uppercase;
  }
  .address span { display: block; letter-spacing: 4.4px; }
  .divider { position: absolute; left: 300px; top: 311px; width: 2px; height: 109px; background: var(--blue); }
  .attendance {
    position: absolute; left: 345px; top: 401px;
    font-family: "Lexend Exa", sans-serif; font-weight: 300; font-size: 19px; line-height: 1; letter-spacing: 15px;
  }
  .deadline-band {
    position: absolute; left: 0; top: 443px; width: 680px; height: 24px;
    background: var(--pink); clip-path: polygon(0 0, 100% 0, 98.5% 100%, 0 100%);
    font-family: "Montserrat", sans-serif; font-weight: 700; font-size: 16px; line-height: 24px;
    padding-left: 36px; text-transform: uppercase; letter-spacing: .3px;
  }
  .contact, .welcome {
    position: absolute; top: 477px;
    font-family: "Montserrat", sans-serif; font-weight: 500; font-size: 12.5px; line-height: 16px;
  }
  .contact { left: 34px; display: flex; align-items: center; gap: 7px; }
  .welcome { left: 334px; text-transform: uppercase; letter-spacing: .4px; }
</style>
</head>
<body>
  <main class="postcard">
    <div class="dancer-figure" role="img" aria-label="Silhouette of a leaping dancer in a pink-to-violet gradient"></div>

    <p class="presenter">Brightreel Productions presents<br>Nora Jean Ashby’s</p>

    <svg class="title" width="800" height="240" viewBox="0 0 800 240" aria-label="Leap, Pulse Stride">
      <defs>
        <linearGradient id="titleGradient" x1="34" y1="0" x2="630" y2="0" gradientUnits="userSpaceOnUse">
          <stop offset="0" stop-color="#0a56b8"/>
          <stop offset=".2" stop-color="#0b64c0"/>
          <stop offset=".5" stop-color="#08d4d8"/>
          <stop offset=".64" stop-color="#4a9ad0"/>
          <stop offset=".8" stop-color="#d80d74"/>
          <stop offset="1" stop-color="#d80d74"/>
        </linearGradient>
      </defs>
      <g transform="skewX(-12)">
        <text x="62" y="124" font-family="'Krona One', sans-serif" font-size="48" fill="#fff"
              textLength="440" lengthAdjust="spacingAndGlyphs">LEAP,PULSE</text>
        <text x="82" y="234" font-family="'Krona One', sans-serif" font-size="124" fill="url(#titleGradient)"
              textLength="585" lengthAdjust="spacingAndGlyphs">STRIDE</text>
      </g>
    </svg>

    <p class="auditions">Auditions</p>

    <svg class="schedule" width="800" height="533" viewBox="0 0 800 533" aria-label="30th June 2022, Thursday 6:30-8:30 PM">
      <text x="34" y="375" font-family="'Oswald', sans-serif" font-weight="500" font-size="83" fill="#08d4d8"
            textLength="69" lengthAdjust="spacingAndGlyphs">30</text>
      <text x="109" y="334" font-family="'Oswald', sans-serif" font-weight="500" font-size="33" fill="#08d4d8"
            textLength="29" lengthAdjust="spacingAndGlyphs">TH</text>
      <text x="150" y="332" font-family="'Krona One', sans-serif" font-size="31" fill="#d80d74"
            textLength="105" lengthAdjust="spacingAndGlyphs">2022</text>
      <text x="109" y="373" font-family="'Krona One', sans-serif" font-size="42" fill="#fff"
            textLength="150" lengthAdjust="spacingAndGlyphs">JUNE</text>
      <text x="339" y="336" font-family="'Krona One', sans-serif" font-size="34" fill="#fff"
            textLength="244" lengthAdjust="spacingAndGlyphs">THURSDAY</text>
      <text x="338" y="390" font-family="'Oswald', sans-serif" font-weight="500" font-size="53" fill="#08d4d8"
            textLength="247" lengthAdjust="spacingAndGlyphs">6:30-8:30 PM</text>
    </svg>

    <p class="address">4172 Kestrel BLVD,<span>Oakland CA 94605</span></p>

    <div class="divider"></div>

    <div class="attendance">IN PERSON</div>

    <div class="deadline-band">Video submissions turn in by Sunday July 3rd, 2022</div>

    <p class="contact">
      <svg width="16" height="11" viewBox="0 0 16 11" aria-hidden="true">
        <rect x="0.5" y="0.5" width="15" height="10" fill="#1f63c6" stroke="#1f63c6"/>
        <path d="M0.5 0.5 L8 6 L15.5 0.5 M0.5 10.5 L6 5 M15.5 10.5 L10 5" fill="none" stroke="#0b0d2e" stroke-width="1"/>
      </svg>
      LeapPulseStride22@movenote.test
    </p>
    <p class="welcome">Teens and adults welcomed</p>
  </main>
</body>
</html>
```